Web Design Project for Landscaping Company

We want a web design for our company based in Grand Rapids, Michigan.

We are a commercial landscaping company working for corporate, companies and government clients.

We are specialized in blueprint landscaping execution. Based on the drawings (or blueprints) from an architect, we install trees, pavers, retaining walls, sod, etc.

Our projects range from schools, hospitals, office buildings, to franchised restaurants such as Rico Fern, Dumarks, etc. We also do landscaping for new retail stores such as Holtons, Brisdowns, or KTQ pharmacies. We do not do mowing or landscape maintenance. We are highly specialized and our clients are large construction companies that outsource the landscaping work for new projects or construction to us.

We want a webpage that the design is based on simplicity, modernism, and with art photography, such as close-up and large images with very high resolution.

We are very tech driven. In a market that there are lots of mom & pops companies, we are a medium size. We strive to do everything electronically without use of paper. All our documents are store online and we are proud as we are in the vanguard of technology compared to others in our industry.

I like the designs created by this company, which it uses a lot of photography to express simplicity in its designs:

www.imarbelvo.example

Hence, our future website has to portray:
- simplicity
- modern company
- tech driven
- professionalism
- tech driven

Our name is Stonebay Landscaping Inc. The name means that we do "green" work and other work as well ("Plus") such as pavers, retaining wall, irrigation, slope restoration, etc. The name was carefully selected and the logo and branding was done with a professional designed.

Reason: Based on the current holiday period and festivities, we are extending the deadline.

Target Market(s)

B2B and B2G

Industry/Entity Type

Construction

Requirements
Must have
• 1. DESIGN:
- Art photography (black and white is an option)

- Minimum writing. None likes to read anymore. So, I want to say more with images and less with words

2. CMS: Content Management System, so we can edit and modify the content on a need basis.
Nice to have
• Structure: Front Page + Services & Products page + contact page + gallery projects (before and after)

```html
<!DOCTYPE html>
<html lang="en">
<head>
<meta charset="utf-8">
<title>Stonebay Landscaping Inc. – Landing Page</title>
<link rel="stylesheet" href="https://fonts.googleapis.com/css2?family=Arimo:wght@400;700&family=Tinos&display=swap">
<style>
:root{
  --bar:#242424;
  --header:#f1f1f1;
  --green:#6cb61d;
  --page:#dcdcdc;
  --white:#fff;
  --line:#d8d8d8;
  --text:#333;
}
*{box-sizing:border-box;margin:0;padding:0}
html,body{width:758px;height:1200px;overflow:hidden}
body{position:relative;background:var(--page);font-family:Arimo,Arial,sans-serif;color:var(--text);font-size:9px}
.abs{position:absolute}
.topbar{left:0;top:0;width:758px;height:28px;background:var(--bar);color:#ddd;font-size:8.5px}
.topbar span{position:absolute;top:10px}
.header{left:0;top:28px;width:758px;height:87px;background:var(--header)}
.brand{font-weight:700;color:var(--green);letter-spacing:-.5px}
.brand-main{left:56px;top:60px;font-size:33px;line-height:1}
.brand-main i{display:inline-block;width:14px;height:14px;background:var(--green);margin-left:5px;vertical-align:top}
.nav{left:265px;top:79px;display:flex;gap:8px}
.nav a{display:block;height:36px;background:linear-gradient(#3b3b3b,#222);color:#fff;text-decoration:none;padding:6px 0 0 9px;font-family:Tinos,Georgia,serif;font-size:10.5px;border-radius:2px 2px 0 0;box-shadow:2px 2px 4px rgba(0,0,0,.25)}
.nav a small{display:block;font-family:Arimo,Arial,sans-serif;font-size:6.5px;margin-top:3px}
.nav a .caret{color:#888;font-size:7px;margin-left:4px}
.nav a.on{color:var(--green)}
.nav a.on small{color:#fff}
.subbar{left:0;top:115px;width:758px;height:37px;background:linear-gradient(#2e2e2e,#1c1c1c)}
.social{left:56px;top:126px;display:flex;gap:4px}
.social span{width:15px;height:15px;border-radius:50%;background:#2e2e2e;border:1px solid #555}
.search-top{left:567px;top:126px;width:134px;height:15px;border-radius:8px;background:#3a3a3a;color:#ddd;font-size:8px;padding:3px 8px}
.search-top svg{position:absolute;right:8px;top:3px}
.hero-band{left:0;top:152px;width:758px;height:274px;background:var(--green)}
.hero-box{left:56px;top:175px;width:646px;height:227px;background:var(--white);box-shadow:0 2px 6px rgba(0,0,0,.3)}
.hero-frame{left:67px;top:190px;width:407px;height:196px;border:1px solid var(--line);box-shadow:inset 0 0 0 3px #f6f6f6}
.hero-photo{left:80px;top:203px;width:386px;height:171px;
  background:
   radial-gradient(ellipse 60px 45px at 56% 22%,rgba(255,250,200,.95),rgba(220,240,150,.5) 50%,rgba(0,0,0,0)),
   linear-gradient(180deg,#1e4010 0%,#3d7a22 30%,#2a5a14 48%,#3f8f1c 60%,#6cc42e 100%)}
.hero-side{left:482px;top:190px;width:204px;height:192px;border:1px solid var(--line)}
.brand-hero{left:493px;top:232px;font-size:29px;line-height:1}
.brand-hero i{display:inline-block;width:12px;height:12px;background:var(--green);margin-left:4px;vertical-align:top}
.hero-text{left:490px;top:287px;width:189px;font-size:7.5px;line-height:12px;color:#333}
.main{left:56px;top:451px;width:646px;height:665px;background:var(--white)}
.crumbs{left:56px;top:451px;width:646px;height:28px;background:var(--bar);color:#fff;font-size:8px}
.crumbs .home{position:absolute;left:10px;top:10px;color:var(--green)}
.crumbs .dot{position:absolute;left:39px;top:12px;width:4px;height:4px;border-radius:50%;background:#ccc}
.crumbs .here{position:absolute;left:52px;top:10px}
.crumbs .tip{position:absolute;left:118px;top:0;width:0;height:0;border-top:14px solid transparent;border-bottom:14px solid transparent;border-left:10px solid #3a3a3a}
.login{left:577px;top:457px;width:76px;height:15px;border-radius:8px;background:#111;color:#fff;font-size:8px;padding:3px 10px;border:1px solid #444}
.sizes{left:664px;top:458px;color:#fff;font-family:Arimo,Arial,sans-serif}
.sidebar{left:502px;top:479px;width:200px;height:637px;background:linear-gradient(90deg,#e4e4e4,#fff 12px)}
.content h1{position:absolute;left:67px;top:500px;font-weight:400;font-size:23px;color:#111}
.intro{left:67px;top:529px;width:424px;font-size:8.5px;line-height:1.4}
.tools{left:465px;top:492px;display:flex;gap:6px}
.feature{left:80px;top:573px;width:396px;height:263px;
  background:
   radial-gradient(ellipse 140px 60px at 45% 78%,rgba(240,240,235,.85),rgba(0,0,0,0)),
   radial-gradient(ellipse 120px 80px at 85% 40%,rgba(120,90,60,.8),rgba(0,0,0,0)),
   linear-gradient(180deg,#6f6a64 0%,#a89c8a 18%,#e0c89a 34%,#8e7c66 46%,#cfd0cc 62%,#7c7268 80%,#3e3630 100%)}
.thumbs{left:71px;top:840px;display:grid;grid-template-columns:repeat(4,96px);column-gap:10.5px;row-gap:3px}
.thumbs div{height:64px}
.t-shore{background:radial-gradient(ellipse 40px 14px at 45% 70%,rgba(235,235,230,.8),rgba(0,0,0,0)),linear-gradient(#5f5a55,#c8b08a 35%,#a8a49c 60%,#4a403a)}
.t-bridge{background:linear-gradient(170deg,#3e4b72,#c4566a 30%,#8a6c88 52%,#b0824a 58%,#3a4a6a)}
.t-pier{background:linear-gradient(#2e3a5a,#8a96b6 35%,#e8d2a6 52%,#9eb0c8 70%,#56688a)}
.t-night{background:radial-gradient(ellipse 40px 10px at 60% 72%,rgba(240,170,70,.9),rgba(0,0,0,0)),linear-gradient(#1a2850,#34487a 60%,#1e2a44)}
.t-arch{background:radial-gradient(ellipse 30px 14px at 45% 45%,rgba(70,50,40,.85),rgba(0,0,0,0)),linear-gradient(#34406c,#e0a070 48%,#9a7a78 62%,#4a4a62)}
.t-mist{background:linear-gradient(#4a5470,#c0b8c8 40%,#9ec0cc 60%,#6a8aa0)}
.prev{left:69px;top:1060px;width:34px;height:20px;border:1px solid var(--line);color:var(--green);font-size:7.5px;padding:5px 0 0 5px;background:#fff}
.rule{left:67px;top:1094px;width:424px;height:1px;background:#eee}
.side-search{left:510px;top:487px;width:183px;height:34px;background:var(--bar)}
.side-search span{position:absolute;left:8px;top:8px;width:146px;height:18px;background:#eee;border:1px solid #ccc;font-size:8px;padding:4px 7px;color:#333}
.side-frame{left:510px;top:530px;width:184px;height:546px;background:#fff;border:1px solid var(--line)}
.side-photo{left:519px;top:542px;width:166px;height:523px;
  background:
   linear-gradient(125deg,rgba(0,0,0,0) 55%,rgba(120,200,30,.9) 68%,rgba(210,240,170,.7) 74%,rgba(60,150,20,.9) 82%,rgba(0,0,0,0) 92%),
   radial-gradient(ellipse 120px 200px at 40% 25%,#c8e08a,rgba(0,0,0,0)),
   linear-gradient(180deg,#9cc85a,#7fb33a 50%,#6a9a32)}
.footer{left:0;top:1138px;width:758px;height:62px;background:var(--bar)}
.brand-foot{left:56px;top:1162px;font-size:15px}
.brand-foot i{display:inline-block;width:7px;height:7px;background:var(--green);margin-left:2px;vertical-align:top}
.copy{left:426px;top:1155px;color:#fff;font-size:8px}
.foot-links{left:598px;top:1173px;color:var(--green);font-size:8px;word-spacing:3px}
.to-top{left:674px;top:1158px;width:27px;height:20px;border:1px solid #444;background:#111}
</style>
</head>
<body>
<div class="abs topbar"><span style="left:56px">Call Toll Free:1.800.555.0142</span><span style="right:56px">418 Orchard Lane, Maplewood, MI 49501</span></div>
<header class="abs header"></header>
<div class="abs brand brand-main">Stonebay<i></i></div>
<nav class="abs nav">
  <a href="#" style="width:57px">Home<span class="caret">▾</span><small>Welcome</small></a>
  <a href="#" class="on" style="width:73px">Landing Page<small>Example Static</small></a>
  <a href="#" style="width:72px">Our Services<small>Services we offer</small></a>
  <a href="#" style="width:72px">Products<small>Products we offer</small></a>
  <a href="#" style="width:58px">Media<span class="caret">▾</span><small>Media Center</small></a>
  <a href="#" style="width:65px">Contact Us<small>Get in touch</small></a>
</nav>
<div class="abs subbar"></div>
<div class="abs social"><span></span><span></span><span></span><span></span></div>
<div class="abs search-top">Search...<svg width="8" height="8" viewBox="0 0 8 8"><circle cx="3.2" cy="3.2" r="2.3" fill="none" stroke="#ddd" stroke-width="1.2"/><line x1="5" y1="5" x2="7.5" y2="7.5" stroke="#ddd" stroke-width="1.2"/></svg></div>

<section class="abs hero-band"></section>
<div class="abs hero-box"></div>
<div class="abs hero-frame"></div>
<div class="abs hero-photo" role="img" aria-label="Sunlit park with tall trees and green lawn"></div>
<div class="abs hero-side"></div>
<div class="abs brand brand-hero">Stonebay<i></i></div>
<p class="abs hero-text">Lorem ipsum dolor sit amet, consectetur adipiscing elit. Praesent semper varius urna tristique ultrices. Vestibulum id nisi tortor, ac ornare nisl. Duis sagittis tortor a nisi aliquam eu sodales sapien blandit. Suspendisse ut urna est, at cursus orci. Mauris quam eros, viverra a vestibulum at, vestibulum et nibh, iverra a vestibulum at, vestibulum et nibh</p>

<main class="abs main"></main>
<div class="abs sidebar"></div>
<div class="abs crumbs"><span class="home">Home</span><span class="dot"></span><span class="here">Landing Page</span><span class="tip"></span></div>
<div class="abs login">Login &nbsp;Register</div>
<div class="abs sizes"><span style="font-size:8px">A</span> <span style="font-size:10px">A</span> <span style="font-size:12px">A</span></div>

<article class="content">
  <h1>Stonebay Landscaping, Inc.</h1>
  <div class="abs tools">
    <svg width="10" height="8" viewBox="0 0 10 8"><rect x=".5" y=".5" width="9" height="7" fill="none" stroke="#999"/><path d="M.5 .5 5 4.5 9.5 .5" fill="none" stroke="#999"/></svg>
    <svg width="10" height="9" viewBox="0 0 10 9"><rect x="2.5" y=".5" width="5" height="3" fill="none" stroke="#999"/><rect x=".5" y="3.5" width="9" height="4" fill="none" stroke="#999"/></svg>
  </div>
  <p class="abs intro">Consectetur adipiscing elit. Praesent semper varius urna tristique ultrices. Vestibulum id nisi tortor, ac ornare nisl. Duis sagittis tortor a nisi aliquam eu sodales sapien blandit.</p>
  <div class="abs feature" role="img" aria-label="Rocky coastline with sea stacks and misty waves under a golden evening sky"></div>
  <div class="abs thumbs">
    <div class="t-shore" role="img" aria-label="Rocky shore at sunset"></div>
    <div class="t-bridge" role="img" aria-label="Suspension bridge under a red dusk sky"></div>
    <div class="t-pier" role="img" aria-label="Old pier in calm water"></div>
    <div class="t-night" role="img" aria-label="Bridge and city lights at night"></div>
    <div class="t-arch" role="img" aria-label="Sea arch at sunset"></div>
    <div class="t-mist" role="img" aria-label="Pier posts in misty water"></div>
    <div class="t-shore" role="img" aria-label="Rocky shore at sunset"></div>
    <div class="t-bridge" role="img" aria-label="Suspension bridge under a red dusk sky"></div>
    <div class="t-pier" role="img" aria-label="Old pier in calm water"></div>
    <div class="t-night" role="img" aria-label="Bridge and city lights at night"></div>
    <div class="t-arch" role="img" aria-label="Sea arch at sunset"></div>
    <div class="t-mist" role="img" aria-label="Pier posts in misty water"></div>
  </div>
  <div class="abs prev">&lt; Prev</div>
  <div class="abs rule"></div>
</article>

<aside>
  <div class="abs side-search"><span>Search...</span></div>
  <div class="abs side-frame"></div>
  <div class="abs side-photo" role="img" aria-label="Close-up of curving green grass blades on a soft green background"></div>
</aside>

<footer class="abs footer"></footer>
<div class="abs brand brand-foot">Stonebay<i></i></div>
<div class="abs copy">Copyright © 2012. Stonebay Landscaping Inc. Designed by CMS</div>
<div class="abs foot-links">Admin Sitemap</div>
<div class="abs to-top"><svg width="27" height="20" viewBox="0 0 27 20"><path d="M9.5 12 13.5 8 17.5 12" fill="none" stroke="#fff" stroke-width="1.3"/></svg></div>
</body>
</html>
```